Flyer for New Spa Opening

We need a flyer to increase customer's awareness of our new spa located in Yangon, Myanmar, in a middle-upper class shopping mall. A new hotel will be opening above the mall in Dec 2013.
Updates

Have made payment guaranteed.  Need a good flyer. Thanks.

Hi, I have uploaded a Words File for Flyer Text. Thanks!

Dear Designers,

I have setup a 2nd award, there's too many outstanding designs! Thanks so much.

Regards
Odile

Target Market(s)

-Hotel guest who wants to a spa session to relax
-Woman between 18 - 55 years old who have high spending power in a poor country(Myanmar). They like to use "Big Brands" but do not have much variety available in their country.

Industry/Entity Type

Shopping

Requirements
Must have
• Our services include Body Spa, Facial, Nails, Waxing & Foot Reflexology. We use well-known international brands in our spa including Veloranthe, KUV, Marven, Brenzo Lativa and TORVE.

Veloranthe, the skin care system researched and developed by The Halvering Dermal Academy (HDA), is an international leader in today’s skin care industry.

We are authorized Veloranthe skin spa to provide professional facial and retailing Veloranthe products.

Include the logo of the brands

Quellmoor Spa
add: No 82, Kelvash Road, Morrin Plaza (Level-5) (7168), Dagon Township, Yangon
tel: +959 62087315
email: contactus@vertlane-holdco.example

Nice to have
• visually nice and relaxing spa pictures.
Should not have
• price

```html
<!DOCTYPE html>
<html lang="en">
<head>
<meta charset="utf-8">
<title>Quellmoor Spa – Brochure Spread</title>
<link href="https://fonts.googleapis.com/css2?family=Arimo:wght@400;700&family=Parisienne&family=Shadows+Into+Light&display=swap" rel="stylesheet">
<style>
  :root{
    --stage:#e9e9ea;
    --pink-pale:#f9dfe7;
    --pink-soft:#f2bfce;
    --pink-mid:#e98fab;
    --rose:#d9305a;
    --rose-deep:#b3173e;
    --heading:#df4f7c;
    --text:#555;
    --muted:#777;
    --white:#fff;
  }
  *{box-sizing:border-box;margin:0;padding:0}
  html,body{width:1200px;height:1000px;overflow:hidden;background:var(--stage)}
  body{font-family:"Arimo",Arial,sans-serif;color:var(--text);position:relative}

  .brochure{
    position:absolute;left:40px;top:95px;width:1120px;height:810px;
    background:linear-gradient(160deg,var(--pink-pale) 0%,var(--pink-soft) 55%,var(--pink-mid) 100%);
    box-shadow:0 6px 22px rgba(0,0,0,.18);overflow:hidden;
  }
  .petal-backdrop{position:absolute;inset:0;
    background:radial-gradient(circle at 96% 20%,rgba(217,48,90,.35),transparent 12%),
               radial-gradient(circle at 98% 70%,rgba(217,48,90,.3),transparent 10%),
               radial-gradient(circle at 70% 3%,rgba(217,48,90,.25),transparent 8%);}

  /* cover */
  .cover{position:absolute;left:0;top:0;width:375px;height:100%;
    background:linear-gradient(180deg,#f7d3de 0%,#f4c4d2 45%,#fbe7ee 62%,#fff 68%);}
  .cover-petals{position:absolute;left:0;top:0;width:100%;height:60%;
    background:radial-gradient(circle at 30% 20%,rgba(200,60,90,.28),transparent 25%),
               radial-gradient(circle at 75% 40%,rgba(200,60,90,.22),transparent 22%),
               radial-gradient(circle at 20% 55%,rgba(200,60,90,.18),transparent 20%);}
  .cover-location{position:absolute;right:22px;top:30px;font-size:14px;color:var(--white)}
  .cover-location b{font-weight:400;font-size:18px}
  .cover-title{position:absolute;left:0;right:0;top:318px;text-align:center;
    font-family:"Parisienne",cursive;font-weight:400;font-size:58px;color:var(--white);}
  .cover-photo{position:absolute;left:0;bottom:0;width:100%;height:280px;
    background:linear-gradient(180deg,#fff 0%,#f6c9c8 30%,#e05a6d 70%,#c3203f 100%);}

  /* inside */
  .inside{position:absolute;left:380px;top:28px;width:700px;height:742px;background:var(--white);
    display:flex;gap:16px;padding:0 16px 0 0;overflow:hidden}
  .col{position:relative}
  .col-main{width:360px;flex:0 0 360px}
  .col-side{width:308px;flex:0 0 308px;padding-top:10px;display:flex;flex-direction:column}

  .photo{background:linear-gradient(135deg,#e9e3e3,#f3d6dc 50%,#c9a8a4);}
  .photo-facial{width:360px;height:215px;border:3px solid var(--white);outline:1px solid #ddd}
  .brand-row{display:flex;justify-content:flex-end;padding:4px 4px 2px;border-bottom:1px solid #ccc;margin-left:40px}
  .brand{font-family:"Arimo",Arial,sans-serif;font-weight:700;color:#444;font-size:17px;letter-spacing:.5px}

  .section{padding-left:40px}
  .heading{font-family:"Shadows Into Light",cursive;font-weight:400;color:var(--heading);font-size:18px;line-height:1.05;margin-top:6px}
  p{font-size:12.5px;line-height:1.3}
  .col-side .heading{font-size:17px;margin-top:5px}
  .col-side p{font-size:11.5px;line-height:1.25}
  .col-side p.includes{font-size:9px;color:var(--muted);margin-top:2px;line-height:1.2}
  .italic{font-style:italic}

  .products{display:flex;gap:30px;align-items:flex-end;margin:10px 0 6px 40px}
  .product{display:flex;flex-direction:column;align-items:center;gap:4px}
  .bottles{width:100px;height:48px;background:linear-gradient(90deg,#eee,#fafafa,#e4e4e4);border-radius:4px}
  .bottles.colour{width:110px;height:44px;background:linear-gradient(90deg,#1b4f9c,#c0213a 35%,#d92a2a 60%,#f2c418)}
  .brand-small{font-size:13px;font-weight:700;color:#333}

  .body-spa{display:flex;align-items:center;gap:22px}
  .body-spa .brand-small{font-size:12px}

  .side-item{display:flex;gap:8px;align-items:flex-start}
  .photo-scrub{flex:0 0 85px;height:85px;margin-top:6px;background:linear-gradient(135deg,#d9b58a,#f1e4d0 60%,#8a6a4a)}
  .photo-feet{width:200px;height:88px;margin:8px 0 4px 40px;background:linear-gradient(135deg,#3a1c18,#a8635a 50%,#c33 100%)}
</style>
</head>
<body>
<section class="brochure">
  <div class="petal-backdrop" role="img" aria-label="Scattered rose petals on pink background"></div>

  <div class="cover">
    <div class="cover-petals" role="img" aria-label="Falling rose petals"></div>
    <div class="cover-location">Located in <b>Yangon, Myanmar</b></div>
    <h1 class="cover-title">Quellmoor Spa</h1>
    <div class="cover-photo" role="img" aria-label="Hands holding red rose petals"></div>
  </div>

  <div class="inside">
    <div class="col col-main">
      <div class="photo photo-facial" role="img" aria-label="Therapist applying a facial mask"></div>
      <div class="brand-row"><span class="brand">veloranthe</span></div>

      <div class="section">
        <h2 class="heading">Facial:</h2>
        <p>We are authorized Veloranthe skin spa to provide Professional Facial and Retailing Veloranthe products. Veloranthe, the skin care system from US, researched and developed by The Halvering Dermal Academy (HDA), is an international leader in today's skin care industry. Chose from a Customized Facial or Targeted Treatment Facial. Customized Facial is designed to address every client's skin type and concern. Our professionally trained therapists will careful select the product and procedure that is most suitable for your skin to achieve true skin health. Targeted Treatment includes LumaClear® Facial, AgeRenew® Facial, CalmSoothe™ Facial and PureBalance™ Facial. Tell us your skin concern and we have the solution just for you!</p>
      </div>

      <div class="products">
        <div class="product"><div class="bottles" role="img" aria-label="Gel polish bottles"></div><span class="brand-small">Marven</span></div>
        <div class="product"><span class="brand-small">KUV</span><div class="bottles colour" role="img" aria-label="Nail lacquer bottles"></div></div>
      </div>

      <div class="section">
        <h2 class="heading">Nails:</h2>
        <p class="italic">We know you love KUV! We have over 200 choices of KUV colours just for you. Our Nail Technicians are trained to provide the most meticulous Manicure &amp; Pedicure according to the Professional System by KUV.</p>
        <div class="body-spa">
          <h2 class="heading">Body Spa:</h2>
          <span class="brand-small">TORVE</span>
          <span class="brand-small">Brenzo Lativa</span>
        </div>
        <p class="italic">Indulge your body, mind and soul in one of our relaxing Spa Treatments</p>
      </div>
    </div>

    <div class="col col-side">
      <h2 class="heading">Quellmoor Day Spa (2.5hr)</h2>
      <p>A luxurious spa experience designed for total relaxation. A delightful body scrub will leave your skin smooth to the touch, followed by a 60min Swedish Aromatherapy massage. The treatment is complete with a body wrap to nourish your skin and your head gently massaged, giving you a profound sense of pleasure and well-being.</p>
      <p class="includes">Includes: Body Scrub · 60min Swedish Aromatherapy Massage · Body Wrap with Head Massage</p>

      <h2 class="heading">Traditional Body Massage (1.5hr)<br>Swedish Aromatherapy Body Massage (1.5hr)</h2>
      <div class="side-item">
        <div>
          <h2 class="heading">Revitalizing Body Scrub (1hr)</h2>
          <p>Your skin is polished smooth and soft to the touch followed by a luxurious body cream massaged in to hydrate the newly revealed skin.</p>
          <p class="includes">Includes: Body Scrub · Light Body Massage</p>
        </div>
        <div class="photo photo-scrub" role="img" aria-label="Body scrub jars and towel"></div>
      </div>

      <h2 class="heading">Pampering Body Treatment (1.5hr)</h2>
      <p>An all over body treatment begins with a body scrub to exfoliate dead skin, in preparation for a body wrap that restores your skin to youthful condition. Lastly a luxurious body cream is massaged in leaving your skin beautifully radiant.</p>
      <p class="includes">Includes: Body Scrub · Body Wrap with Head Massage · Light Body Massage</p>

      <h2 class="heading">Foot Massage (1hr)</h2>
      <p>Pamper your foot that has taken you a hundred miles. Following a foot soak and cleaning, we will begin foot massage on your foot reflex zones stimulating body energy and on your muscles to soothe tired heavy legs.</p>
      <p class="includes">Includes: Foot Soak · Foot Massage</p>
      <div class="photo photo-feet" role="img" aria-label="Feet resting in a bowl of rose petals"></div>

      <h2 class="heading">Waxing</h2>
      <p>We take care of all the unsightly hairy body parts, just leave it to us. Walk out like a new sexy you!</p>
    </div>
  </div>
</section>
</body>
</html>
```